We are full service plumbing contractors that are capable of performing all of your plumbing need...

A clean, crisp website that conveys we can handle any plumbing from drain cleaning, repairs, to new construction. But emphasis on Leak detection, under-slab and underground water service leaks, repairs, and reroutes. Leak detection by acoustical, Thermal, or tracer gas , methods.Also emphasize advanced drain cleaning technologies and equipment. Don't just poke ahole in the drain blockage, Clean the pipe, with our High pressure hydrojetters, or Chain knocker drain cables that expand to the width of the pipe being cleaned.

Number of Pages Required

5+ page

Font styles to use
Sans Serif

Requirements
Should not have
• Canned photos

```html
<!DOCTYPE html>
<html lang="en">
<head>
<meta charset="utf-8">
<title>Tidewell Plumbing – Plumbing &amp; Leak Detection</title>
<link href="https://fonts.googleapis.com/css2?family=Montserrat:wght@400;500;600;700&family=Poppins:wght@300;400;500;600&display=swap" rel="stylesheet">
<style>
:root{
  --blue:#1a73c4;
  --navy:#2a2470;
  --deep:#0b0b35;
  --yellow:#f2b01e;
  --ink:#1b1b1b;
  --muted:#6d6d6d;
  --white:#ffffff;
}
*{box-sizing:border-box;margin:0;padding:0}
html,body{width:1200px;height:3805px;overflow:hidden}
body{font-family:"Poppins",sans-serif;color:var(--ink);background:var(--white);position:relative}
.abs{position:absolute}
section,header,footer{position:absolute;left:0;width:1200px}

/* header */
.site-header{top:0;height:120px;background:var(--blue)}
.brand{left:0;top:0;width:240px;height:120px;background:var(--white);display:flex;align-items:center;justify-content:center;gap:8px}
.brand-dot{width:12px;height:12px;border-radius:50%;background:var(--blue);flex:none}
.brand-name{font-family:"Montserrat",sans-serif;font-weight:700;font-size:19px;color:var(--navy);white-space:nowrap}
.nav{left:410px;top:0;height:120px;display:flex;align-items:center;gap:60px;font-size:14px;color:var(--white)}
.nav .active{color:#7fd0ff}
.call{right:40px;top:36px;text-align:right;color:var(--white)}
.call strong{font-family:"Montserrat",sans-serif;font-size:20px;font-weight:700}
.call strong span{color:var(--yellow)}
.call small{display:block;font-size:14px;margin-top:2px}

/* hero */
.hero{top:120px;height:480px;background:linear-gradient(135deg,#5a4a3c 0%,#3b3029 45%,#786a5e 100%)}
.hero-text{top:135px;left:0;width:1200px;text-align:center;color:var(--white);font-family:"Montserrat",sans-serif}
.hero-text h1{font-size:38px;font-weight:700;line-height:1.2}
.hero-text h1 em{display:block;font-style:normal;color:var(--yellow);font-size:52px;text-decoration:underline;text-decoration-thickness:3px;text-underline-offset:6px}
.btn{display:inline-block;font-family:"Montserrat",sans-serif;font-weight:600;font-size:13px}
.hero .btn{position:absolute;left:472px;top:329px;width:256px;height:38px;line-height:38px;text-align:center;background:var(--blue);color:var(--white)}

/* booking */
.booking{top:600px;height:480px}
.booking-left{left:0;top:0;width:600px;height:480px;background:linear-gradient(120deg,#f3f5f8,#dfe4ea)}
.booking-right{left:600px;top:0;width:600px;height:480px;background:var(--navy)}
.eyebrow{font-family:"Montserrat",sans-serif;font-size:14px;font-weight:600;color:var(--blue);display:flex;align-items:center;gap:10px}
.eyebrow svg{width:20px;height:20px}
.booking-left .eyebrow{position:absolute;left:120px;top:82px}
.booking-left p{position:absolute;left:120px;top:128px;width:318px;font-size:16px;line-height:32px;color:#555}
.btn-navy{background:var(--navy);color:var(--white);text-align:center}
.booking-left .btn{position:absolute;left:120px;top:357px;width:120px;height:42px;line-height:42px}
.booking-right .eyebrow{position:absolute;left:120px;top:82px;color:var(--yellow)}
.field{position:absolute;height:40px;background:var(--white);font-size:10px;color:#9a9a9a;padding:12px 14px;letter-spacing:1px}
.field.msg{height:98px}
.send{position:absolute;left:120px;top:360px;width:120px;height:40px;line-height:40px;background:var(--yellow);color:var(--white);text-align:center}

/* services */
.services{top:1080px;height:648px}
.services .eyebrow{position:absolute;left:0;width:1200px;top:78px;justify-content:center}
.services h2{position:absolute;top:120px;left:0;width:1200px;text-align:center;font-family:"Montserrat",sans-serif;font-weight:500;font-size:30px;line-height:1.28}
.tile{position:absolute;top:272px;width:300px;height:376px;color:var(--white)}
.tile h3{position:absolute;left:30px;bottom:40px;font-family:"Montserrat",sans-serif;font-size:18px;font-weight:600;line-height:1.35}
.tile.featured{background:linear-gradient(180deg,#2c2a6e,#24214f)}
.tile.featured h3{top:75px;bottom:auto;left:40px}
.tile.featured p{position:absolute;left:40px;top:140px;width:230px;font-size:12px;line-height:1.6}
.tile.featured .more{position:absolute;left:40px;top:295px;font-size:13px;color:#7fb3ff}

/* about */
.about{top:1728px;height:880px}
.about .eyebrow{position:absolute;left:0;width:1200px;top:80px;justify-content:center}
.about h2{position:absolute;top:120px;left:0;width:1200px;text-align:center;font-family:"Montserrat",sans-serif;font-weight:600;font-size:30px;line-height:1.28}
.about-photo{left:120px;top:274px;width:360px;height:525px;background:linear-gradient(160deg,#9c948a,#5d564d 60%,#3e3a33)}
.stats{left:358px;top:309px;width:242px;height:452px;background:var(--navy)}
.stat{height:113px;display:flex;align-items:center;gap:18px;padding-left:22px;border-bottom:1px solid rgba(255,255,255,.2);color:var(--white)}
.stat:last-child{border-bottom:none}
.stat-icon{width:52px;height:52px;border-radius:50%;background:var(--blue);display:flex;align-items:center;justify-content:center}
.stat-icon svg{width:24px;height:24px}
.stat b{font-family:"Montserrat",sans-serif;font-size:22px;color:var(--yellow);display:block}
.stat span{font-size:11px;color:#8fc0ff;line-height:1.3;display:block}
.about-copy{left:720px;top:302px;width:360px}
.about-copy h3{font-family:"Montserrat",sans-serif;font-weight:500;font-size:19px;line-height:1.45;color:var(--blue)}
.about-copy p{margin-top:22px;font-size:12px;line-height:1.8;color:#666;text-align:justify}
.about .btn{position:absolute;left:720px;top:723px;width:120px;height:42px;line-height:42px}

/* testimonial */
.reviews{top:2608px;height:477px;background:var(--blue);color:var(--white);text-align:center}
.reviews .eyebrow{position:absolute;left:0;width:1200px;top:80px;justify-content:center;color:var(--yellow)}
.reviews blockquote{position:absolute;left:200px;width:800px;top:140px;font-size:19px;line-height:28px}
.avatar{left:565px;top:282px;width:70px;height:70px;border-radius:50%;background:linear-gradient(#f0cfa8,#c99a6b);border:3px solid var(--white)}
.reviewer{top:368px;left:0;width:1200px;font-family:"Montserrat",sans-serif}
.reviewer b{font-size:16px;display:block;letter-spacing:1px}
.reviewer span{font-size:11px;letter-spacing:1px}
.arrow{top:307px;width:20px;height:20px}

/* cta */
.cta{top:3085px;height:241px;background:linear-gradient(100deg,#3a342c,#57493a 50%,#2d2823)}
.cta h2{position:absolute;left:120px;top:80px;font-family:"Montserrat",sans-serif;font-size:30px;font-weight:600;color:var(--white)}
.cta p{position:absolute;left:120px;top:120px;width:760px;font-size:15px;line-height:1.35;color:var(--white)}
.cta-circle{left:958px;top:58px;width:124px;height:124px;border-radius:50%;background:var(--blue);box-shadow:0 0 0 12px rgba(26,115,196,.35);color:var(--white);display:flex;align-items:center;justify-content:center;text-align:center;font-family:"Montserrat",sans-serif;font-size:12px;font-weight:600;line-height:1.6}

/* footer */
.site-footer{top:3326px;height:479px;background:var(--deep);color:var(--white)}
.foot-brand{left:250px;top:112px;width:220px;text-align:center}
.foot-brand .brand-name{color:var(--yellow);font-size:21px}
.foot-brand small{display:block;margin-top:22px;font-size:11px;line-height:1.5;color:#4b8fe0}
.foot-contact{left:480px;top:92px;width:240px;text-align:center}
.foot-contact h4{font-family:"Montserrat",sans-serif;color:var(--blue);font-size:14px}
.foot-contact .phone{font-family:"Montserrat",sans-serif;font-size:22px;color:var(--blue);margin-top:12px}
.foot-contact .phone span{color:var(--white)}
.foot-contact small{display:block;font-size:11px;line-height:1.5;color:#4b8fe0}
.foot-contact address{font-style:normal;margin-top:14px;font-size:11px;line-height:1.5;color:#4b8fe0}
.foot-book{left:756px;top:138px;width:166px;height:40px;line-height:38px;border:1px solid var(--blue);text-align:center;font-size:12px;color:var(--blue)}
.social{left:800px;top:200px;display:flex;gap:10px}
.social span{width:14px;height:14px;border:1.5px solid var(--blue);border-radius:3px}
.foot-bottom{left:0;width:1200px;top:355px;text-align:center;font-size:14px;line-height:1.6}
.foot-bottom a{color:var(--blue)}
</style>
</head>
<body>

<header class="site-header">
  <div class="brand abs"><span class="brand-dot"></span><span class="brand-name">Tidewell Plumbing</span></div>
  <nav class="nav abs"><span class="active">Home</span><span>About</span><span>Services</span><span>Review</span><span>Contact</span></nav>
  <div class="call abs"><strong>Call. <span>(555) 203-4196</span></strong><small>Same Day Service Guaranteed!</small></div>
</header>

<section class="hero" role="img" aria-label="Photo of white PVC pipes being repaired in an excavated trench">
  <div class="hero-text abs"><h1>Water Damage, Mold,<br>Leak Detection &amp; Plumbing<em>Experts.</em></h1></div>
  <span class="btn">Book Now (555) 203-4196</span>
</section>

<section class="booking">
  <div class="booking-left abs" role="img" aria-label="Faint photo of a plumber at work behind the text">
    <div class="eyebrow"><svg viewBox="0 0 20 20" fill="none" stroke="#1a73c4" stroke-width="1.6"><path d="M6 9v9H2V9zM6 17h8l3-7V8h-6l1-5-2-1-4 7"/></svg>Same Day Service –</div>
    <p>25 years Experience so you can have confidence the job will be done correctly. Call the Tidewell Experts. We Guarantee Our Work!</p>
    <span class="btn btn-navy">Hire Us</span>
  </div>
  <div class="booking-right abs">
    <div class="eyebrow"><svg viewBox="0 0 20 20" fill="none" stroke="#f2b01e" stroke-width="1.6"><rect x="2" y="4" width="16" height="14"/><path d="M6 2v4M14 2v4M6 11l3 3 5-5"/></svg>Schedule a Service –</div>
    <div class="field" style="left:120px;top:135px;width:172px">NAME</div>
    <div class="field" style="left:308px;top:135px;width:172px">EMAIL</div>
    <div class="field" style="left:120px;top:189px;width:172px">PHONE</div>
    <div class="field" style="left:308px;top:189px;width:172px">DATE</div>
    <div class="field msg" style="left:120px;top:247px;width:360px">MESSAGE ...</div>
    <span class="btn send">Send</span>
  </div>
</section>

<section class="services">
  <div class="eyebrow"><svg viewBox="0 0 20 20" fill="none" stroke="#1a73c4" stroke-width="1.6"><path d="M13 2a5 5 0 0 0-5 6L2 14l4 4 6-6a5 5 0 0 0 6-5l-3 3-3-1-1-3z"/></svg>Services We Provide –</div>
  <h2>We are full service plumbing contractors<br>that are capable of performing all<br>of your plumbing need...</h2>
  <div class="tile" style="left:0;background:linear-gradient(160deg,#4a5a3a,#3a3026)" role="img" aria-label="Photo of a drain cleaning machine beside an open pit"><h3>Blocked Drain<br>Cleaning</h3></div>
  <div class="tile featured" style="left:300px">
    <h3>Leak Detection &amp;<br>Pipe Tracing</h3>
    <p>Our engineers are trained and experienced in using various types of leak detection equipment.</p>
    <span class="more">⊕ More</span>
  </div>
  <div class="tile" style="left:600px;background:linear-gradient(160deg,#6a6056,#3b342c)" role="img" aria-label="Photo of an exposed pipe in an excavated slab"><h3>Underground Slab<br>Leak Repair</h3></div>
  <div class="tile" style="left:900px;background:linear-gradient(160deg,#6e675f,#423b33)" role="img" aria-label="Photo of a repaired water line with a valve"><h3>Water Line Repair<br>&amp; Reroute</h3></div>
</section>

<section class="about">
  <div class="eyebrow"><svg viewBox="0 0 20 20" fill="none" stroke="#1a73c4" stroke-width="1.6"><circle cx="10" cy="6" r="4"/><path d="M2 19c0-5 4-7 8-7s8 2 8 7"/></svg>Who We Are –</div>
  <h2>Delivering plumbing, drain cleaning,<br>repairs, to new construction<br>in USA since 1980</h2>
  <div class="about-photo abs" role="img" aria-label="Photo of a plumber working with a green hose beside a block wall"></div>
  <div class="stats abs">
    <div class="stat"><div class="stat-icon"><svg viewBox="0 0 24 24" fill="none" stroke="#fff" stroke-width="1.8"><circle cx="8" cy="8" r="3"/><circle cx="16" cy="8" r="3"/><path d="M2 19c0-4 3-6 6-6s6 2 6 6M12 13c1-.5 2-1 4-1 3 0 6 2 6 6"/></svg></div><div><b>35+</b><span>Qualified Expert<br>Staffs</span></div></div>
    <div class="stat"><div class="stat-icon"><svg viewBox="0 0 24 24" fill="none" stroke="#fff" stroke-width="1.8"><path d="M15 3a5 5 0 0 0-5 6l-7 7 4 4 7-7a5 5 0 0 0 6-5l-3 3-3-1-1-3z"/></svg></div><div><b>7,500+</b><span>Repairs Last 12<br>Months</span></div></div>
    <div class="stat"><div class="stat-icon"><svg viewBox="0 0 24 24" fill="none" stroke="#fff" stroke-width="1.8"><path d="M6 4h12l4 6-10 11L2 10zM2 10h20M9 4l3 17 3-17"/></svg></div><div><b>25+</b><span>Years Average<br>Experience</span></div></div>
    <div class="stat"><div class="stat-icon"><svg viewBox="0 0 24 24" fill="none" stroke="#fff" stroke-width="1.8"><path d="M7 11v10H3V11zM7 20h9l4-8V10h-7l1-6-2-1-5 8"/></svg></div><div><b>1000+</b><span>Happy<br>Customer</span></div></div>
  </div>
  <div class="about-copy abs">
    <h3>Tidewell Plumbing full service plumbing contractors that are capable of performing all of your plumbing need...</h3>
    <p>Every job starts with a careful inspection so we can find the real cause of the problem and fix it the first time, using modern tools and proven methods on homes and businesses alike.</p>
    <p>From hydro jetting and chain knocker cables to acoustic, thermal and tracer gas leak detection, our crews arrive fully equipped. We repair slab leaks, replace water lines, reroute failing pipes and leave every site clean and tidy before we go.</p>
  </div>
  <span class="btn btn-navy">Hire Us</span>
</section>

<section class="reviews">
  <div class="eyebrow"><svg viewBox="0 0 20 20" fill="none" stroke="#f2b01e" stroke-width="1.6"><circle cx="10" cy="10" r="8"/><path d="M6 12c1 2 7 2 8 0M7 8h0M13 8h0"/></svg>What Our Customer Says –</div>
  <blockquote>“ The overall experience was beyond my expectations.<br>I would definitely recommend them to anyone looking for emergency<br>plumbers lorem ipsum has been the industry's standard<br>dummy text ever ...</blockquote>
  <svg class="arrow abs" style="left:460px" viewBox="0 0 20 20" fill="none" stroke="#cfe3ff" stroke-width="2"><path d="M13 4l-6 6 6 6"/></svg>
  <svg class="arrow abs" style="left:720px" viewBox="0 0 20 20" fill="none" stroke="#cfe3ff" stroke-width="2"><path d="M7 4l6 6-6 6"/></svg>
  <div class="avatar abs" role="img" aria-label="Customer portrait"></div>
  <div class="reviewer abs"><b>MARLA,</b><span>CEDAR HILLS, CA</span></div>
</section>

<section class="cta" role="img" aria-label="Photo of black drain cable coiled on gravel beside an open pipe">
  <h2>Don't just poke ahole in the drain blockage,</h2>
  <p>Clean the pipe, with our High pressure hydro-jets, or Chain knocker drain cables that expand to the width of the pipe being cleaned.</p>
  <div class="cta-circle abs">Contact Us<br>Today!</div>
</section>

<footer class="site-footer">
  <div class="foot-brand abs"><span class="brand-name">Tidewell Plumbing</span><small>Copyright © 2019 Tidewell Plumbing<br>All rights reserved.</small></div>
  <div class="foot-contact abs">
    <h4>Emergency</h4>
    <div class="phone">P. <span>(555) 203-4196</span></div>
    <small>e. hello@tidewellplumbing.example</small>
    <address>Tidewell Plumbing<br>2210 Elm Ridge Ln<br>Suite 4, Fairview<br>CA 90000</address>
  </div>
  <div class="foot-book abs">Book Your Service</div>
  <div class="social abs"><span></span><span></span><span></span><span></span></div>
  <div class="foot-bottom abs">Customer Satisfaction. Our Top Priority.<br><a>Contact Us Today!</a></div>
</footer>

</body>
</html>
```